I need a business card design for a Boutique Pilates studio.

I would like to see designs similar to the one that I have uploaded.
thinking between two slogans:
'No ordinary place'
'Not so ordinary'

Contact Information for Business Card

Keva Pilates

```html
<!DOCTYPE html>
<html lang="en">
<head>
<meta charset="utf-8">
<title>Keva Pilates – Business Card</title>
<link href="https://fonts.googleapis.com/css2?family=Montserrat:wght@400;700&display=swap" rel="stylesheet">
<style>
  :root {
    --backdrop: #1c1c1c;
    --card: #000000;
    --accent: #f2d81c;
    --text-light: #f4f4f4;
  }
  * { margin: 0; padding: 0; box-sizing: border-box; }
  html, body {
    width: 1200px; height: 801px; overflow: hidden;
    background: var(--backdrop);
    font-family: "Montserrat", Arial, sans-serif;
  }
  .stage {
    width: 1200px; height: 801px;
    display: flex; align-items: center; justify-content: center; gap: 40px;
  }
  .card {
    position: relative;
    width: 540px; height: 309px;
    background: var(--card);
    border-left: 1.5px solid var(--accent);
    border-bottom: 1.5px solid var(--accent);
    box-shadow: 0 18px 40px rgba(0,0,0,.6);
    overflow: hidden;
  }
  .brand-name {
    font-family: "Montserrat", Arial, sans-serif;
    font-weight: 400;
    color: var(--accent);
    letter-spacing: 1px;
    white-space: nowrap;
  }

  /* contact side */
  .card--info .brand {
    position: absolute; left: 30px; top: 0; bottom: 0; width: 240px;
    display: flex; align-items: center; justify-content: center;
  }
  .card--info .brand-name { font-size: 28px; }
  .divider {
    position: absolute; left: 282px; top: 70px;
    width: 1.5px; height: 170px; background: var(--accent);
  }
  .contact {
    position: absolute; left: 304px; top: 70px; width: 220px;
    color: var(--text-light);
  }
  .contact-name {
    font-weight: 700; font-size: 21px; color: var(--accent); line-height: 1.1;
  }
  .contact-title { font-size: 11px; margin-top: 3px; }
  .contact-address { font-size: 11px; line-height: 1.35; margin-top: 14px; }
  .contact-list { list-style: none; margin-top: 12px; }
  .contact-list li {
    display: flex; align-items: center; gap: 7px;
    font-size: 11px; line-height: 1.75;
  }
  .contact-list svg { width: 11px; height: 11px; flex: none; }

  /* brand side */
  .card--logo .brand {
    position: absolute; inset: 0;
    display: flex; align-items: center; justify-content: center;
  }
  .card--logo .brand-name { font-size: 48px; }
</style>
</head>
<body>
<main class="stage">
  <section class="card card--info" aria-label="Business card, contact side">
    <div class="brand">
      <span class="brand-name">Keva Pilates</span>
    </div>
    <div class="divider"></div>
    <div class="contact">
      <p class="contact-name">Dana Whitfield</p>
      <p class="contact-title">Managing Director</p>
      <p class="contact-address">418 Linden Ave, #12<br>Brookfield, OH 43210</p>
      <ul class="contact-list">
        <li>
          <svg viewBox="0 0 12 12" aria-hidden="true"><circle cx="6" cy="6" r="6" fill="#f2d81c"/><path d="M4 3.2l1 1.4-.6.7a4 4 0 0 0 2.3 2.3l.7-.6 1.4 1-.6 1a5.5 5.5 0 0 1-5.2-5.2z" fill="#000"/></svg>
          555-318-2047
        </li>
        <li>
          <svg viewBox="0 0 12 12" aria-hidden="true"><circle cx="6" cy="6" r="6" fill="#f2d81c"/><rect x="3" y="4" width="6" height="4.2" fill="#000"/><path d="M3 4l3 2.3L9 4" stroke="#f2d81c" stroke-width=".7" fill="none"/></svg>
          hello@kevapilates.example
        </li>
        <li>
          <svg viewBox="0 0 12 12" aria-hidden="true"><circle cx="6" cy="6" r="6" fill="#f2d81c"/><circle cx="6" cy="6" r="3.2" fill="none" stroke="#000" stroke-width=".8"/><path d="M2.8 6h6.4M6 2.8c-1.4 1.8-1.4 4.6 0 6.4M6 2.8c1.4 1.8 1.4 4.6 0 6.4" stroke="#000" stroke-width=".7" fill="none"/></svg>
          www.kevapilates.example
        </li>
      </ul>
    </div>
  </section>

  <section class="card card--logo" aria-label="Business card, brand side">
    <div class="brand">
      <span class="brand-name">Keva Pilates</span>
    </div>
  </section>
</main>
</body>
</html>
```